New Website

New website is to be the same as Copper Lantern.

Website needs to be fully functional, with only text and logo to be added by client at a later date.

Logo has been added for reference.

Reason: waiting for the final submissions to be completed.

```html
<!DOCTYPE html>
<html lang="en">
<head>
<meta charset="utf-8">
<title>Veltra — The Right Expert, Right Now</title>
<link rel="stylesheet" href="https://fonts.googleapis.com/css2?family=Roboto:ital,wght@0,300;0,400;0,500;0,700;1,400&display=swap">
<style>
:root{
  --ink:#2b2b2b;
  --text:#3a3a3a;
  --muted:#666;
  --white:#fff;
  --brand:#3a5fb0;
  --brand-light:#5fb7d8;
  --nav-bar:#6f6f6f;
  --nav-dark:#2f2f2f;
  --band-dark:#444;
  --band-mid:#4a4a4a;
  --light-bg:#f4f4f4;
  --grey-bg:#dcdcdc;
  --footer-1:#444;
  --footer-2:#595959;
  --footer-3:#737373;
}
*{box-sizing:border-box;margin:0;padding:0}
html,body{width:1200px;height:2778px;overflow:hidden;background:var(--white)}
body{font-family:'Roboto',Arial,sans-serif;color:var(--text)}
.page{position:relative;width:1200px;height:2778px;overflow:hidden;background:var(--white)}
.abs{position:absolute}

/* header */
.site-header{position:absolute;left:0;top:0;width:1200px;height:100px}
.header-bar{position:absolute;left:0;top:61px;width:1200px;height:39px;background:linear-gradient(#7a7a7a,#5e5e5e)}
.brand{position:absolute;left:186px;top:14px;display:flex;align-items:center;gap:12px}
.brand-mark{width:66px;height:66px;border-radius:50%;background:var(--white);border:4px solid #e6e6e6;box-shadow:0 2px 4px rgba(0,0,0,.25)}
.brand-name{font-size:38px;font-weight:400;color:var(--brand);letter-spacing:2px;line-height:1}
.brand-tag{position:absolute;left:78px;top:52px;font-size:10px;color:var(--brand-light);white-space:nowrap}
.main-nav{position:absolute;left:466px;top:34px;display:flex;gap:27px;font-size:15px;color:var(--ink)}
.auth{position:absolute;left:838px;top:25px;display:flex;align-items:center;gap:10px;font-size:12px;color:var(--muted)}
.auth .btn-sm{background:var(--nav-dark);color:var(--white);padding:6px 16px}
.expert-cta{position:absolute;left:653px;top:61px;width:176px;height:39px;background:var(--nav-dark);color:var(--white);font-size:16px;display:flex;align-items:center;justify-content:center;gap:10px}
.find-cta{position:absolute;left:836px;top:61px;width:182px;height:46px;background:var(--brand);color:var(--white);font-size:17px;display:flex;align-items:center;justify-content:center;gap:10px}

/* hero */
.hero{position:absolute;left:0;top:100px;width:1200px;height:387px;background:var(--white)}
.hero-photo{position:absolute;left:537px;top:0;width:663px;height:337px;background:linear-gradient(90deg,#f2f2f2,#d9d9d9 55%,#c6c6c6)}
.hero-person{position:absolute;left:532px;top:0;width:480px;height:410px;background:linear-gradient(#cfcfcf,#a9a9a9)}
.hero-title{position:absolute;left:203px;top:92px;font-size:31px;line-height:38px;font-weight:400;color:var(--ink)}
.hero-sub{position:absolute;left:203px;top:196px;font-size:21px;color:var(--ink)}
.btn-dark{display:inline-flex;align-items:center;gap:8px;background:var(--nav-dark);color:var(--white);font-size:12px;padding:0 14px;height:24px}
.hero .btn-dark{position:absolute;left:203px;top:257px}
.dots{position:absolute;left:278px;top:336px;display:flex;gap:4px}
.dots span{width:7px;height:7px;border-radius:50%;background:#777}

/* testimonial */
.testimonials{position:absolute;left:0;top:487px;width:1200px;height:280px;background:var(--band-dark);color:var(--white);text-align:center}
.testimonials h2{position:absolute;left:0;right:0;top:62px;font-size:24px;font-weight:400}
.quote{position:absolute;left:296px;width:608px;top:114px;font-size:13.5px;font-style:italic;line-height:21px;color:#ddd}
.author{position:absolute;left:0;right:0;top:207px;font-size:17px}
.author-role{position:absolute;left:0;right:0;top:231px;font-size:10px;color:#ccc}
.arrow{position:absolute;top:125px}

/* video */
.video{position:absolute;left:0;top:767px;width:1200px;height:340px;background:var(--light-bg)}
.video h2{position:absolute;left:0;right:0;top:34px;text-align:center;font-size:29px;font-weight:400;color:var(--ink)}
.video-frame{position:absolute;left:291px;top:100px;width:618px;height:278px;background:var(--white);padding:4px;box-shadow:0 4px 8px rgba(0,0,0,.25)}
.video-still{width:100%;height:100%;background:linear-gradient(120deg,#d8dde0,#b9b3aa 45%,#e3e3e3)}
.play{position:absolute;left:281px;top:118px;width:56px;height:38px;background:rgba(30,30,30,.85);border-radius:4px}

/* experts */
.experts{position:absolute;left:0;top:1107px;width:1200px;height:556px;background:linear-gradient(#e4e4e4,#d6d6d6)}
.experts h2{position:absolute;left:0;right:0;top:78px;text-align:center;font-size:24px;font-weight:400;color:var(--ink)}
.expert-band{position:absolute;left:0;top:230px;width:1200px;height:154px;background:var(--band-mid)}
.expert{position:absolute;top:152px;width:220px;color:var(--white)}
.expert-photo{width:137px;height:133px;border:3px solid var(--white);background:linear-gradient(#c9c9c9,#9e9e9e)}
.expert-name{margin-top:20px;font-size:17px;font-weight:700}
.expert-role{font-size:13px;line-height:15px}
.experts-note{position:absolute;left:236px;width:728px;top:418px;text-align:center;font-size:17px;line-height:22px;color:var(--ink)}
.experts .btn-dark{position:absolute;left:541px;top:506px}

/* how it works */
.how{position:absolute;left:0;top:1663px;width:1200px;height:552px}
.how h2{position:absolute;left:0;right:0;top:46px;text-align:center;font-size:24px;font-weight:400;color:var(--ink)}
.how-intro{position:absolute;left:0;right:0;top:94px;text-align:center;font-size:13px;color:var(--ink)}
.step{position:absolute;top:170px;width:200px;text-align:center}
.step svg{display:block;margin:0 auto}
.step h3{margin-top:28px;font-size:23px;font-weight:400;line-height:29px;color:var(--ink)}
.step p{margin-top:12px;font-size:11px;line-height:15px;color:var(--text)}
.slash{position:absolute;top:278px}
.how .btn-dark{position:absolute;left:543px;top:479px}

/* footer */
.site-footer{position:absolute;left:181px;top:2215px;width:838px;height:491px;display:flex}
.foot-col{width:279px;height:100%;position:relative;color:var(--white)}
.foot-links{background:var(--footer-1);padding:34px 20px}
.foot-links a{display:block;color:var(--white);text-decoration:none;font-size:35px;line-height:47px;font-weight:300}
.foot-blog{background:var(--footer-2);padding:38px 34px;text-align:center}
.foot-blog h3{font-size:29px;font-weight:400;line-height:34px}
.post{margin-top:24px;font-size:11px;line-height:15px}
.post .q{font-size:22px;font-weight:700;vertical-align:-6px}
.post-date{margin-top:6px;font-weight:700;font-size:10.5px}
.post-by{font-weight:700;font-style:italic;font-size:10.5px}
.foot-help{background:var(--footer-3);padding:38px 20px}
.foot-help h3{font-size:29px;font-weight:400}
.foot-help p{font-size:10.5px;line-height:15px;margin-top:14px;color:#eee}
.foot-help h3.mt{margin-top:34px}
.social{display:flex;gap:5px;margin-top:18px}
.social span{width:33px;height:33px;border-radius:50%;background:#2e6fb8;border:2px solid var(--white)}
.legal{position:absolute;left:181px;top:2735px;font-size:10px;color:var(--ink)}
</style>
</head>
<body>
<div class="page">

  <header class="site-header">
    <div class="header-bar"></div>
    <div class="brand">
      <div class="brand-mark"></div>
      <span class="brand-name">VELTRA</span>
      <span class="brand-tag">advisors for business growth</span>
    </div>
    <nav class="main-nav"><span>How it Works</span><span>Products</span><span>Blog</span><span>Help</span></nav>
    <div class="auth"><span class="btn-sm">Sign In</span><span>OR</span><span class="btn-sm">Register</span></div>
    <div class="expert-cta">
      <svg width="10" height="7" viewBox="0 0 10 7"><path d="M0 0h10L5 7z" fill="#fff"/></svg>Make Me An Expert
    </div>
    <div class="find-cta">
      <svg width="17" height="17" viewBox="0 0 17 17"><circle cx="7" cy="7" r="5.2" fill="none" stroke="#fff" stroke-width="2.4"/><path d="M11 11l4.5 4.5" stroke="#fff" stroke-width="2.6" stroke-linecap="round"/></svg>Find Your Expert
    </div>
  </header>

  <section class="hero">
    <div class="hero-photo" role="img" aria-label="Bright office meeting room in soft grey tones"></div>
    <div class="hero-person" role="img" aria-label="Smiling consultant in shirt and tie seated behind a laptop"></div>
    <h1 class="hero-title">The Right Expert,<br>Right Now™</h1>
    <p class="hero-sub">Consulting Made Simple</p>
    <span class="btn-dark">Browse Business Categories <svg width="5" height="8" viewBox="0 0 5 8"><path d="M1 1l3 3-3 3" stroke="#fff" fill="none"/></svg></span>
    <div class="dots"><span></span><span></span><span></span></div>
  </section>

  <section class="testimonials">
    <h2>What Clients Are Saying</h2>
    <svg class="arrow" style="left:206px" width="16" height="30" viewBox="0 0 16 30"><path d="M14 2L2 15l12 13" stroke="#fff" stroke-width="2" fill="none"/></svg>
    <p class="quote">I felt this session was on target and the solutions we discussed are real candidates. We are only one discussion away from recommending a winning plan. Owen Hale was articulate, knowledgeable, experienced, and concise. Very helpful!</p>
    <p class="author">Mara Ellison</p>
    <p class="author-role">—CEO, the circuit loft</p>
    <svg class="arrow" style="left:980px" width="16" height="30" viewBox="0 0 16 30"><path d="M2 2l12 13L2 28" stroke="#fff" stroke-width="2" fill="none"/></svg>
  </section>

  <section class="video">
    <h2>Watch The Video</h2>
    <div class="video-frame">
      <div class="video-still" role="img" aria-label="Team of four colleagues reviewing documents around a meeting table"></div>
      <svg class="play" viewBox="0 0 56 38"><path d="M22 11l14 8-14 8z" fill="#fff"/></svg>
    </div>
  </section>

  <section class="experts">
    <h2>Introducing Your Business Expert Network</h2>
    <div class="expert-band"></div>
    <div class="expert" style="left:226px">
      <div class="expert-photo" role="img" aria-label="Portrait of expert Dana Whitlock"></div>
      <p class="expert-name">Dana Whitlock</p>
      <p class="expert-role">CEO • Northwind Reach, Inc.<br>Cloudline Services</p>
    </div>
    <div class="expert" style="left:430px">
      <div class="expert-photo" role="img" aria-label="Portrait of expert Robin Castell"></div>
      <p class="expert-name">Robin Castell</p>
      <p class="expert-role">Senior Director<br>Market Research</p>
    </div>
    <div class="expert" style="left:634px">
      <div class="expert-photo" role="img" aria-label="Portrait of expert Ray Fenwick"></div>
      <p class="expert-name">Ray Fenwick</p>
      <p class="expert-role">Principal<br>Strategic Messaging</p>
    </div>
    <div class="expert" style="left:837px">
      <div class="expert-photo" role="img" aria-label="Portrait of expert Jill Moran"></div>
      <p class="expert-name">Jill Moran</p>
      <p class="expert-role">Chief Operating Officer<br>Manufacturing Strategy</p>
    </div>
    <p class="experts-note">All of our experts meet high qualification requirements and undergo rigorous testing for their specific skills and consulting abilities. Learn more about how experts are chosen. If you think you have what it takes, become an expert today.</p>
    <span class="btn-dark">See All Experts <svg width="5" height="8" viewBox="0 0 5 8"><path d="M1 1l3 3-3 3" stroke="#fff" fill="none"/></svg></span>
  </section>

  <section class="how">
    <h2>How it Works</h2>
    <p class="how-intro">Find an Expert who's just right for your business need. Your Expert Package includes:</p>

    <div class="step" style="left:256px">
      <svg width="76" height="74" viewBox="0 0 76 74"><path d="M8 14h58v44L52 70H8z" fill="none" stroke="#333" stroke-width="5" stroke-linejoin="round"/><path d="M52 70V58h14" fill="none" stroke="#333" stroke-width="4"/><rect x="28" y="4" width="16" height="24" rx="3" fill="none" stroke="#333" stroke-width="4"/></svg>
      <h3>Pre-Session<br>Discovery</h3>
      <p>Lorem Ipsum has been the industry's standard dummy text ever since the 1500s, when an unknown printer took a galley of type and scrambled it to make a type specimen book.</p>
    </div>
    <svg class="slash" style="left:447px" width="16" height="48" viewBox="0 0 16 48"><path d="M14 2L2 46" stroke="#333" stroke-width="2"/></svg>
    <div class="step" style="left:500px">
      <svg width="76" height="74" viewBox="0 0 76 74"><rect x="8" y="40" width="60" height="8" fill="#333"/><path d="M20 48h36l-6 24H26z" fill="#333"/><rect x="28" y="14" width="20" height="24" rx="3" fill="#333"/><circle cx="38" cy="8" r="6" fill="#333"/></svg>
      <h3>One+-On-One<br>Session</h3>
      <p>Lorem Ipsum has been the industry's standard dummy text ever since the 1500s, when an unknown printer took a galley of type and scrambled it to make a type specimen book.</p>
    </div>
    <svg class="slash" style="left:727px" width="16" height="48" viewBox="0 0 16 48"><path d="M14 2L2 46" stroke="#333" stroke-width="2"/></svg>
    <div class="step" style="left:774px">
      <svg width="96" height="74" viewBox="0 0 96 74"><circle cx="48" cy="8" r="6" fill="#333"/><path d="M38 26a10 10 0 0 1 20 0z" fill="#333"/><circle cx="14" cy="50" r="6" fill="#333"/><path d="M2 70a12 12 0 0 1 24 0z" fill="#333"/><circle cx="82" cy="50" r="6" fill="#333"/><path d="M70 70a12 12 0 0 1 24 0z" fill="#333"/><circle cx="48" cy="44" r="9" fill="none" stroke="#333" stroke-width="6" stroke-dasharray="4 3"/><circle cx="48" cy="44" r="3" fill="#333"/><path d="M24 38q4-12 14-14M58 24q10 2 14 14M34 66q14 6 28 0" fill="none" stroke="#333" stroke-width="2"/></svg>
      <h3>Post-Session<br>Options</h3>
      <p>Lorem Ipsum has been the industry's standard dummy text ever since the 1500s, when an unknown printer took a galley of type and scrambled it to make a type specimen book.</p>
    </div>
    <span class="btn-dark">See How it work <svg width="5" height="8" viewBox="0 0 5 8"><path d="M1 1l3 3-3 3" stroke="#fff" fill="none"/></svg></span>
  </section>

  <footer class="site-footer">
    <div class="foot-col foot-links">
      <a>About Us</a><a>Our Team</a><a>Legal</a><a>Contact Us</a>
    </div>
    <div class="foot-col foot-blog">
      <h3>What We're<br>Thinking</h3>
      <div class="post">
        <p><span class="q">“</span>Lorem Ipsum is simply dummy text of the printing and typesetting industry.<span class="q">”</span></p>
        <p class="post-date">Monday, January 12</p>
        <p class="post-by">Alex Brennard</p>
      </div>
      <div class="post" style="margin-top:36px">
        <p><span class="q">“</span>Lorem Ipsum is simply dummy text of the printing and typesetting industry. Lorem Ipsum has been the industry's standard dummy text ever since the 1500s, when an unknown printer took a galley of type and scrambled it to make a type specimen book. It has survived not only five centuries, but also the leap into electronic typesetting, remaining essentially unchanged.<span class="q">”</span></p>
        <p class="post-date">Monday, January 12</p>
        <p class="post-by">Owen Hale</p>
      </div>
    </div>
    <div class="foot-col foot-help">
      <h3>Need Help?</h3>
      <p>Copper Lantern is committed to providing exceptional cloud-based consulting. If you need help with any aspect of the Copper Lantern experience, please send us a note and we will reply promptly. Or feel free to call our support line between 9am and 5pm Pacific Time.</p>
      <h3 class="mt">Contact Us</h3>
      <p>Copper Lantern, Inc.<br>support@copperlantern.com</p>
      <h3 class="mt">Follow us on</h3>
      <div class="social" aria-label="Social media links"><span></span><span></span><span></span><span></span><span></span></div>
    </div>
  </footer>

  <p class="legal">© 2015 Veltra. Terms of Use and Privacy Policy</p>
</div>
</body>
</html>
```